RW Domestic & Commercial Heating & Plumbing, needs a business card Design

We need a business card design for a company in the United Kingdom, we work mainly in London in Domestic Plumbing & Heating and would like to branch out (more) in to the Commercial aspect of the business.
We need the card to promote care, trust, professionalism, because we do, if possible, we will always better or match prices with an over all better experience for clients.

Info to add on card...

My name... Owen Barclay
Cell... 07491137758
Email... owenbarclay00@Mailvista.com
Business/Post code... SE14 2XJ

Thanks

Owen
Updates

Hi there updated my design project! If you could please look through again and add as much as possable (as you will see) I'd be very grateful! Although I do enjoy seeing all your fantastic designs, I don't want to spend the remaining 14 days being hard to please. PS.. I'm from NZ but living in UK, if you find patriotic (NZ) that is do add in. Not of huge importance but It dose get peoples attention! Thanks a lot, Owen

Target Market(s)

I work in Chelsea and most of my days so think Chelsea.

Thanks.

Industry/Entity Type

Business

Font styles to use
Serif
Sans Serif

Requirements
Must have
• Just want text to be as easy to read as possible!

Would like to see some or all pictures I have on the card if at all possible.
They are well known logos in my industry.
And my team and I are all fully qualified in these different schemes.

Also a break down of services I provide!

- Central Heating Engineering.
- Bathroom and Kitchen Fitting.
- Plumbing.
- Electrical.
- Tiling.
- All Your Carpentry and Building Needs.

Thanks.

Should not have
• Only restriction no pink otherwise go for it!

Thanks.

```html
<!DOCTYPE html>
<html lang="en">
<head>
<meta charset="utf-8">
<title>RW Domestic &amp; Commercial Heating &amp; Plumbing – Business Card</title>
<link rel="stylesheet" href="https://fonts.googleapis.com/css2?family=Roboto+Condensed:wght@400;700&display=swap">
<style>
  :root {
    --brand-blue: #2f5fe0;
    --brand-blue-deep: #2449c4;
    --watermark: rgba(255, 255, 255, 0.14);
    --card-white: #ffffff;
    --page-bg: #e9eaee;
    --badge-orange: #f39200;
    --badge-red: #d7262c;
    --badge-yellow: #ffd400;
    --badge-navy: #1f3a8a;
    --badge-black: #1a1a1a;
  }
  * { box-sizing: border-box; margin: 0; padding: 0; }
  html, body { width: 1200px; height: 873px; overflow: hidden; }
  body {
    background: var(--page-bg);
    font-family: "Roboto Condensed", "Arial Narrow", sans-serif;
    display: flex;
    align-items: center;
    justify-content: center;
    gap: 60px;
  }
  .card {
    position: relative;
    width: 520px;
    height: 336px;
    border-radius: 4px;
    overflow: hidden;
    box-shadow: 0 6px 20px rgba(0, 0, 0, 0.18);
  }

  /* Services side */
  .card--services {
    background: var(--brand-blue);
    color: var(--card-white);
    text-align: center;
  }
  .watermark {
    position: absolute;
    left: 50%;
    top: 50%;
    transform: translate(-50%, -52%);
    font-weight: 700;
    font-size: 300px;
    line-height: 1;
    color: var(--watermark);
    letter-spacing: -10px;
    user-select: none;
  }
  .services {
    position: relative;
    padding-top: 40px;
  }
  .services__title {
    font-weight: 700;
    font-size: 34px;
    margin-bottom: 10px;
  }
  .services__list {
    list-style: none;
    font-size: 24px;
    line-height: 1.3;
  }
  .services__list li::before {
    content: "";
    display: inline-block;
    width: 7px;
    height: 7px;
    border-radius: 50%;
    background: var(--card-white);
    margin-right: 8px;
    vertical-align: middle;
  }
  .services__extra {
    font-size: 24px;
    margin-top: 12px;
  }

  /* Contact side */
  .card--contact { background: var(--card-white); }
  .card__shape {
    position: absolute;
    inset: 0;
    width: 100%;
    height: 100%;
  }
  .brand {
    position: absolute;
    top: 18px;
    left: 0;
    right: 0;
    text-align: center;
    color: var(--card-white);
  }
  .brand__name {
    font-weight: 700;
    font-size: 66px;
    line-height: 1;
  }
  .brand__tagline {
    font-weight: 700;
    font-size: 25px;
    line-height: 1.12;
  }
  .accreditations {
    position: absolute;
    left: 22px;
    bottom: 22px;
    display: grid;
    grid-template-columns: repeat(2, 52px);
    gap: 12px 16px;
  }
  .badge {
    display: block;
    width: 52px;
    height: 24px;
    border-radius: 3px;
  }
  .badge--orange { background: var(--badge-orange); }
  .badge--red { background: var(--badge-red); }
  .badge--yellow { background: var(--badge-yellow); width: 30px; }
  .badge--black { background: var(--badge-black); }
  .badge--navy { background: var(--badge-navy); }
  .contact {
    position: absolute;
    right: 26px;
    bottom: 26px;
    text-align: right;
    color: var(--brand-blue);
    font-size: 19px;
    line-height: 1.3;
  }
  .contact__name {
    font-size: 21px;
    padding-bottom: 4px;
    margin-bottom: 6px;
    border-bottom: 2px solid var(--brand-blue);
    display: inline-block;
  }
</style>
</head>
<body>

  <section class="card card--services" aria-label="Services side">
    <div class="watermark" aria-hidden="true">RW</div>
    <div class="services">
      <h2 class="services__title">Our Services:</h2>
      <ul class="services__list">
        <li>Central Heating Engineering</li>
        <li>Bathroom and Kitchen Fitting</li>
        <li>Plumbing</li>
        <li>Electrical</li>
        <li>Tiling</li>
      </ul>
      <p class="services__extra">All Your Carpentry and Building Needs</p>
    </div>
  </section>

  <section class="card card--contact" aria-label="Contact side">
    <svg class="card__shape" viewBox="0 0 520 336" preserveAspectRatio="none" aria-hidden="true">
      <polygon points="0,0 520,0 520,118 0,196" fill="var(--brand-blue)"/>
      <polygon points="520,300 520,336 470,336" fill="var(--brand-blue)"/>
    </svg>
    <div class="brand">
      <h1 class="brand__name">RW</h1>
      <p class="brand__tagline">Domestic and Commercial<br>Heating &amp; Plumbing</p>
    </div>
    <div class="accreditations" aria-label="Industry accreditations">
      <span class="badge badge--orange"></span>
      <span class="badge badge--red"></span>
      <span class="badge badge--yellow"></span>
      <span class="badge badge--black"></span>
      <span class="badge badge--navy"></span>
    </div>
    <address class="contact" style="font-style: normal;">
      <span class="contact__name">Owen Barclay</span><br>
      M: 07491 137 758<br>
      E: owenbarclay00@mailvista.com<br>
      Postcode: SE14 2XJ
    </address>
  </section>

</body>
</html>
```